NoraB Designs

To have a blog that is interactive and shows products that I produce, with the ability to direct people to ClipVantor and Brimo

I not only do papercrafting but also do sublimition on T-shirts, and other items. I do the designs for all of them. So I need to have pages to decifer these.

I have logo's done. and can provide them.

Target Market(s)

Handmade cards, home projects, sublimiated items (shirts, cups, dog items)

Industry/Entity Type

Gift Shop

Number of Pages Required

4 page

Font styles to use
Serif

Requirements
Must have
• easy to operate for everyone, with good directions, connections to Brimo shop and ClipVantor, along with shopping from suppliers
Nice to have
• I would like the site to be one that clean but happy feeling, one that people will remember and return to. If someone is looking at something specific, maybe a new page to open
Should not have
• a confusing site.

```html
<!DOCTYPE html>
<html lang="en">
<head>
<meta charset="utf-8">
<title>NoraB Designs — Papercraft &amp; Sublimation</title>
<link href="https://fonts.googleapis.com/css2?family=Lobster&family=Roboto+Slab:wght@300;400&family=Roboto:wght@300;400;500&display=swap" rel="stylesheet">
<style>
:root{
  --pink:#fc9f9d;
  --pink-deep:#f98a89;
  --purple:#8f60d2;
  --teal:#5ad3c7;
  --yellow:#fdd96b;
  --peach:#f8c3a4;
  --ink:#3a3535;
  --body:#555;
  --cream:#f7f5f2;
  --white:#fff;
}
*{margin:0;padding:0;box-sizing:border-box}
html,body{width:1200px;height:2486px;overflow:hidden}
body{position:relative;background:var(--white);font-family:'Roboto',sans-serif;color:var(--body)}
.abs{position:absolute}
.script{font-family:'Lobster',cursive;font-weight:400}
.slab{font-family:'Roboto Slab',serif}

/* nav */
.nav{top:0;left:0;width:1200px;height:68px;background:var(--white)}
.nav a{position:absolute;top:28px;font:300 13px 'Roboto Slab',serif;color:var(--ink);text-decoration:none}
.brand{position:absolute;left:530px;top:20px;width:140px;text-align:center;font:400 17px 'Roboto Slab',serif;color:var(--purple)}

/* hero */
.hero{top:68px;left:0;width:1200px;height:525px;background:linear-gradient(180deg,var(--pink) 0%,#fd9a9a 100%);overflow:hidden}
.hero-title{top:43px;width:1200px;text-align:center;font-size:54px;color:var(--white)}
.hero-sub{top:120px;width:1200px;text-align:center;font:300 15px 'Roboto',sans-serif;color:var(--white)}
.flora{border-radius:50%;background:radial-gradient(circle at 50% 50%,#f0636a 0%,#f4868a 45%,rgba(160,190,170,.55) 75%,transparent 76%)}
.cup{border-radius:50%;background:radial-gradient(circle,#e8efe9 0 55%,#7fb39a 56% 70%,rgba(0,0,0,.08) 71%,transparent 80%)}
.card-art{box-shadow:0 10px 30px rgba(0,0,0,.15)}

/* features */
.feature{width:200px}
.feature .icon{width:54px;height:54px;border-radius:50%;display:flex;align-items:center;justify-content:center}
.feature h3{margin-top:14px;font:400 17px 'Roboto Slab',serif;color:var(--ink)}
.feature p{margin-top:10px;font:300 12.5px/19px 'Roboto',sans-serif;color:var(--body)}
.btn{display:block;color:var(--white);font:500 14px 'Roboto',sans-serif;text-align:center;text-decoration:none;border-radius:2px}
.feature .btn{margin-top:20px;width:128px;height:33px;line-height:33px}

.section-title{width:1200px;text-align:center;font-size:31px;color:var(--ink)}
.section-sub{width:1200px;text-align:center;font:300 15px 'Roboto Slab',serif;color:var(--ink)}

.tile{width:282px;height:170px;border-radius:4px;display:flex;align-items:center;justify-content:center;font:400 23px 'Roboto Slab',serif;color:var(--white)}

/* about */
.about{top:1287px;left:0;width:1200px;height:451px;background:var(--cream)}
.about-text{left:497px;top:1417px;width:535px;font:300 12.5px/20.3px 'Roboto',sans-serif;color:var(--ink)}
.about-text p+p{margin-top:15px}

/* blogs */
.post{width:207px;height:308px;background:var(--white);box-shadow:0 4px 14px rgba(0,0,0,.1);border-radius:3px;overflow:hidden}
.post .thumb{height:178px}
.post h4{margin:15px 13px 0;font:400 15px 'Roboto Slab',serif;color:var(--ink)}
.post p{margin:13px 13px 0;font:300 11.5px/17px 'Roboto',sans-serif;color:var(--ink)}
.post .bar{position:absolute;left:0;bottom:0;width:100%;height:4px}

/* footer */
.footer{top:2259px;left:0;width:1200px;height:227px;background:#fb9c9a;color:var(--white)}
.footer h5{position:absolute;top:42px;font:500 17px 'Roboto',sans-serif}
.footer ul{position:absolute;top:80px;list-style:none;font:300 12px/21.7px 'Roboto',sans-serif}
.footer .blurb{position:absolute;top:80px;font:300 12px/19px 'Roboto',sans-serif}
.social li{display:flex;align-items:center;gap:8px}
.social i{display:inline-block;width:7px;height:7px;background:var(--white);border-radius:50%}
.subscribe{position:absolute;left:806px;top:132px;display:flex}
.subscribe span{width:168px;height:25px;background:var(--white);color:#bbb;font:300 10.5px/25px 'Roboto',sans-serif;padding-left:8px}
.subscribe b{width:74px;height:25px;margin-left:2px;background:#f25e6a;font:500 11px/25px 'Roboto',sans-serif;text-align:center}
.rule{position:absolute;top:193px;left:0;width:1200px;height:1px;background:rgba(255,255,255,.35)}
.copy{position:absolute;top:204px;width:1200px;text-align:center;font:300 12px 'Roboto',sans-serif;color:rgba(255,255,255,.8)}
</style>
</head>
<body>

<nav class="nav abs">
  <a style="left:181px">Home</a>
  <a style="left:247px">Papercraft</a>
  <a style="left:337px">Sublimation</a>
  <a style="left:438px">About Me</a>
  <div class="brand">NoraB Designs</div>
  <a style="left:713px">Products I Use</a>
  <a style="left:826px">Blog</a>
  <a style="left:882px">Videos</a>
  <a style="left:953px">Contact</a>
</nav>

<header class="hero abs">
  <div class="flora abs" role="img" aria-label="Watercolour red flowers with green leaves" style="left:-30px;top:-10px;width:230px;height:180px"></div>
  <div class="flora abs" role="img" aria-label="Watercolour red flowers with green leaves" style="left:990px;top:-10px;width:230px;height:185px"></div>
  <div class="cup abs" role="img" aria-label="Cup of tea seen from above" style="left:104px;top:362px;width:50px;height:50px"></div>
  <div class="cup abs" role="img" aria-label="Cup of tea seen from above" style="left:1002px;top:264px;width:52px;height:52px"></div>
  <h1 class="hero-title abs script">Papercraft &amp; Sublimation</h1>
  <p class="hero-sub abs">Lorem ipsum dolor sit amet, consectetur adipiscing&nbsp; sed do eiusmod</p>
  <div class="card-art abs" role="img" aria-label="Handmade floral hello card" style="left:277px;top:244px;width:180px;height:290px;background:linear-gradient(160deg,#f3e8ef,#c9e28a)"></div>
  <div class="card-art abs" role="img" aria-label="Handmade balloon birthday card" style="left:745px;top:244px;width:180px;height:290px;background:linear-gradient(160deg,#d7eef2,#3cbcc0 55%,#f2b533)"></div>
  <div class="card-art abs" role="img" aria-label="Handmade yellow polka-dot happy birthday card" style="left:447px;top:186px;width:302px;height:340px;background:linear-gradient(150deg,#fbe85a,#f7dd3c 60%,#f4efe6)"></div>
</header>

<svg class="abs" style="left:0;top:825px" width="100" height="330" viewBox="0 0 100 330" aria-hidden="true">
  <path d="M0 0 L80 80 Q104 104 96 140 L58 280 Q44 322 0 330 Z" fill="var(--yellow)"/>
</svg>

<section>
  <div class="feature abs" style="left:150px;top:656px">
    <div class="icon" style="background:#f1e9fb"><svg width="22" height="24" viewBox="0 0 22 24" fill="none" stroke="var(--purple)" stroke-width="1.4"><rect x="4" y="2" width="14" height="19" rx="1"/><path d="M7 7h8M7 11h8M7 15h6"/></svg></div>
    <h3>Paper Craft</h3>
    <p>Lorem ipsum dolor avdipiscing elit, ssmod tempor incididunt ut labore dolore magna aliqua.</p>
    <a class="btn" style="background:var(--purple)">Visit Now</a>
  </div>
  <div class="feature abs" style="left:394px;top:656px">
    <div class="icon" style="background:#e6f8f5"><svg width="24" height="22" viewBox="0 0 24 22" fill="none" stroke="var(--teal)" stroke-width="1.4"><path d="M8 2 L2 6 L5 10 L7 9 V20 H17 V9 L19 10 L22 6 L16 2 Q12 6 8 2Z"/></svg></div>
    <h3>Sublimation</h3>
    <p>Lorem ipsum dolor avdipiscing elit, ssmod tempor incididunt ut labore dolore magna aliqua.</p>
    <a class="btn" style="background:var(--teal)">Visit Now</a>
  </div>
  <div class="feature abs" style="left:637px;top:656px">
    <div class="icon" style="background:#fdf4dc"><svg width="24" height="18" viewBox="0 0 24 18" fill="none" stroke="#e8c04a" stroke-width="1.4"><rect x="2" y="2" width="20" height="14" rx="3"/><path d="M10 6 L15 9 L10 12Z"/></svg></div>
    <h3>ClipVantor</h3>
    <p>Lorem ipsum dolor avdipiscing elit, ssmod tempor incididunt ut labore dolore magna aliqua.</p>
    <a class="btn" style="background:var(--yellow)">Visit Now</a>
  </div>
  <div class="feature abs" style="left:880px;top:656px">
    <div class="icon" style="background:#fdeee6"><svg width="20" height="20" viewBox="0 0 20 20" fill="none" stroke="var(--peach)" stroke-width="1.6"><rect x="3" y="3" width="14" height="14"/></svg></div>
    <h3>Brimo</h3>
    <p>Lorem ipsum dolor avdipiscing elit, ssmod tempor incididunt ut labore dolore magna aliqua.</p>
    <a class="btn" style="background:var(--peach)">Visit Now</a>
  </div>
</section>

<section>
  <h2 class="section-title script abs" style="top:942px">Lorem Ipsum</h2>
  <p class="section-sub abs" style="top:996px">Lorem ipsum dolor sit amet, consectetur adipiscing</p>
  <div class="tile abs" role="img" aria-label="Craft desk with tools, tinted yellow" style="left:150px;top:1056px;background:linear-gradient(135deg,#fbd75f,#fde27a)">Videos</div>
  <div class="tile abs" role="img" aria-label="Handmade cards laid out, tinted peach" style="left:459px;top:1056px;background:linear-gradient(135deg,#f9c2a6,#fbcfb6)">Blogs</div>
  <div class="tile abs" role="img" aria-label="Teacher with children in a class, tinted teal" style="left:768px;top:1056px;background:linear-gradient(135deg,#5ccfc4,#7fdcd2)">Online Classes</div>
</section>

<section class="about abs"></section>
<div class="abs" role="img" aria-label="Green leafy branch" style="left:0;top:1287px;width:100px;height:108px;background:radial-gradient(ellipse at 30% 40%,#5ea84a,#8cc56e 50%,transparent 72%)"></div>
<svg class="abs" style="left:1104px;top:1250px" width="96" height="328" viewBox="0 0 96 328" aria-hidden="true">
  <path d="M96 0 L96 328 L20 250 Q0 228 8 196 L52 44 Q64 6 96 0 Z" fill="var(--purple)"/>
</svg>
<div class="abs" role="img" aria-label="Portrait of the designer in front of green foliage" style="left:150px;top:1346px;width:278px;height:335px;border-radius:4px;box-shadow:0 6px 20px rgba(0,0,0,.15);background:linear-gradient(180deg,#3d6b3a 0%,#5f8a4d 35%,#e8c7a3 70%,#ece0d8 100%)"></div>
<h2 class="script abs" style="left:497px;top:1349px;font-size:31px;color:var(--ink)">About Me</h2>
<div class="about-text abs">
  <p>Well, NoraB is a mother of three grown children, a daughter and two sons a daughter-in-law, and a grandmother of two gorgeous little ones, both are very special to me. Plus, one more on it way! I am currently on sick leave from work, due to an automobile accident last year. One being a concussion, and mobility of my neck.&nbsp; I also live with several disorders, Crohn's, Gastroparesis, Arterial Septal Defect, just to name a few. But, these don't get me down, unless you put me in the hospital and disrupt my days. That is right, I hate to be disrupted.</p>
  <p>The cards that I make are donated. I donate or give them to people all the time. I carry them with me most times, and share them with those willing to share. So making cards, and donating them has been very good for me.</p>
</div>
<a class="btn abs" style="left:497px;top:1636px;width:167px;height:45px;line-height:45px;background:var(--yellow);font-size:15px">Read More</a>

<section>
  <h2 class="section-title script abs" style="top:1785px">Latest Blogs</h2>
  <p class="section-sub abs" style="top:1840px">Lorem ipsum dolor sit amet, consectetur adipiscing</p>

  <article class="post abs" style="left:156px;top:1900px">
    <div class="thumb" role="img" aria-label="Green botanical birthday card" style="background:linear-gradient(135deg,#5a4a3c,#a8c9ad 30%,#e9efe8)"></div>
    <h4>Birthday Card</h4>
    <p>Lorem ipsum dolor sit consectetur adipiscing elit, sed do mod tempor incididunt ut labore</p>
    <div class="bar" style="background:var(--yellow)"></div>
  </article>
  <article class="post abs" style="left:383px;top:1900px">
    <div class="thumb" role="img" aria-label="White mug with printed lettering" style="background:linear-gradient(135deg,#dfe3dc,#f7f6f4 50%,#ece7e4)"></div>
    <h4>Mom Fuel</h4>
    <p>Lorem ipsum dolor sit consectetur adipiscing elit, sed do mod tempor incididunt ut labore</p>
    <div class="bar" style="background:var(--purple)"></div>
  </article>
  <article class="post abs" style="left:610px;top:1900px">
    <div class="thumb" role="img" aria-label="Yellow printed T-shirt with jeans" style="background:linear-gradient(135deg,#e9a526,#f2b62f 55%,#5c7290)"></div>
    <h4>Kind &amp; Humble</h4>
    <p>Lorem ipsum dolor sit consectetur adipiscing elit, sed do mod tempor incididunt ut labore</p>
    <div class="bar" style="background:var(--yellow)"></div>
  </article>
  <article class="post abs" style="left:836px;top:1900px">
    <div class="thumb" role="img" aria-label="Hot air balloon happy birthday card" style="background:linear-gradient(135deg,#eceeed,#a7d6dc 45%,#f4efe6)"></div>
    <h4>Birthday Card</h4>
    <p>Lorem ipsum dolor sit consectetur adipiscing elit, sed do mod tempor incididunt ut labore</p>
    <div class="bar" style="background:var(--purple)"></div>
  </article>
</section>

<footer class="footer abs">
  <h5 style="left:150px">NoraB Designs</h5>
  <p class="blurb" style="left:149px;width:190px">Lorem ipsum dolor sit amet, consectetur adipiscing elit, sed do eiusmod tempor incididunt ut labore et dolore magna aliqua.</p>
  <h5 style="left:386px">Quick Links</h5>
  <ul style="left:387px"><li>Lorem Ipsum</li><li>Lorem Ipsum</li><li>Lorem Ipsum</li><li>Lorem Ipsum</li></ul>
  <h5 style="left:528px">Quick Links</h5>
  <ul style="left:528px"><li>Lorem Ipsum</li><li>Lorem Ipsum</li><li>Lorem Ipsum</li><li>Lorem Ipsum</li></ul>
  <h5 style="left:670px">Follow Me</h5>
  <ul class="social" style="left:671px"><li><i></i>Friendwall</li><li><i></i>Chirpline</li><li><i></i>Snapgrid</li><li><i></i>ClipVantor</li></ul>
  <h5 style="left:807px">Subscribe to Newsletter</h5>
  <p class="blurb" style="left:804px;width:240px">Lorem ipsum dolor sit amet, consectetur adipiscing elit, sed do eiusmod tempor</p>
  <div class="subscribe"><span>Enter your Email</span><b>Subscribe</b></div>
  <div class="rule"></div>
  <p class="copy">Copyright © NoraB Designs 2021</p>
</footer>

</body>
</html>
```